Granite Ridge Holdings

I have a real estate investment business.

** I need editable vector files of the final design.

Industry/Entity Type

Real Estate

Contact Information for Business Card

I would like the card to be clear and direct with the company name and contact info. I would prefer not to have a design that is too busy (i.e., with excessive detail) in the business card.

Font styles to use
Sans Serif

Requirements
Must have
• My card must have the following information listed below:
• Company name: Grainite Ridge Holdings LLC
• My name: Daniel Vorsley
• Phone number: (555) 218-9067
• Email address: dtvorsley@mailbox-example.net
• Keywords: “Real Estate Investments”
Nice to have
• I would like to have a design that resembles the characteristics/uses of obsidian stone which resembles something related to strength and resilience. Perhaps something with sharp, sleek color transitions as well.

```html
<!DOCTYPE html>
<html lang="en">
<head>
<meta charset="utf-8">
<title>Grainite Ridge Holdings LLC – Business Card</title>
<link rel="stylesheet" href="https://fonts.googleapis.com/css2?family=Arimo:ital,wght@0,700;1,700&display=swap">
<style>
  :root {
    --page-bg: #ffffff;
    --obsidian: #000000;
    --slate: #555555;
    --stone-mid: #2a2a2a;
    --stone-front: #16161a;
    --stone-back: #2e2e2e;
    --accent: #e0580f;
    --paper: #ffffff;
    --edge: #6b6b6b;
    --silver: #b5b5b5;
  }
  html, body {
    margin: 0;
    padding: 0;
    width: 1000px;
    height: 1200px;
    overflow: hidden;
    background: var(--page-bg);
  }
  .sheet { display: block; width: 1000px; height: 1200px; }
  .card-text { font-family: "Arimo", Arial, sans-serif; font-weight: 700; }
  .company-line { font-size: 36px; }
  .company-line--top { fill: var(--paper); }
  .company-line--bottom { fill: var(--silver); }
  .holder-name { font-size: 37px; font-style: italic; fill: var(--accent); }
  .holder-role { font-size: 15px; font-style: italic; fill: var(--accent); }
  .contact-line { font-size: 15px; font-style: italic; fill: var(--accent); }
  .back-company { font-size: 37px; font-style: italic; fill: var(--accent); }
  .photo-area--front { fill: var(--stone-front); }
  .photo-area--back { fill: var(--stone-back); }
  .contact-icon { fill: none; stroke: var(--accent); stroke-width: 1.6; stroke-linejoin: round; }
  .contact-icon--solid { fill: var(--accent); stroke: none; }
</style>
</head>
<body>
<svg class="sheet" viewBox="0 0 1000 1200" xmlns="http://www.w3.org/2000/svg">
  <defs>
    <linearGradient id="front-stone" x1="0" y1="0" x2="1" y2="0">
      <stop offset="0" stop-color="var(--obsidian)"/>
      <stop offset="0.55" stop-color="var(--obsidian)"/>
      <stop offset="1" stop-color="var(--slate)"/>
    </linearGradient>
    <linearGradient id="back-stone" x1="0" y1="0" x2="0" y2="1">
      <stop offset="0" stop-color="var(--slate)"/>
      <stop offset="0.45" stop-color="var(--stone-mid)"/>
      <stop offset="0.85" stop-color="var(--obsidian)"/>
    </linearGradient>
  </defs>

  <g class="card card--front">
    <rect x="165" y="124" width="663" height="429" fill="var(--paper)" stroke="var(--edge)" stroke-width="1.5"/>
    <path class="stone-panel" d="M165,124 L828,124 L493,338 C480,450 340,540 165,553 Z" fill="url(#front-stone)"/>
    <ellipse class="photo-area photo-area--front" role="img" aria-label="Photograph of a polished obsidian sphere" cx="364" cy="358" rx="111" ry="138"/>
    <text class="card-text company-line company-line--top" x="387" y="235" text-anchor="middle">Grainite Ridge</text>
    <text class="card-text company-line company-line--bottom" x="387" y="282" text-anchor="middle">Holdings LLC</text>

    <text class="card-text holder-name" x="525" y="357">Daniel Vorsley</text>
    <text class="card-text holder-role" x="527" y="391">Real Estate Investments</text>

    <path class="contact-icon contact-icon--solid" d="M531,413 l4,-1 l3,5 l-2,2 c1,3 3,5 6,6 l2,-2 l5,3 l-1,4 c-9,0 -17,-8 -17,-17 z"/>
    <text class="card-text contact-line" x="556" y="427">(555) 218-9067</text>

    <rect class="contact-icon" x="529" y="446" width="16" height="11"/>
    <path class="contact-icon" d="M529,446 l8,6 l8,-6 M529,457 l6,-5 M545,457 l-6,-5"/>
    <text class="card-text contact-line" x="556" y="457">dtvorsley@mailbox-example.net</text>
  </g>

  <g class="card card--back">
    <rect x="165" y="634" width="663" height="428" fill="url(#back-stone)"/>
    <path class="photo-area photo-area--back" role="img" aria-label="Close-up photograph of an obsidian stone" d="M300,930 C360,850 440,822 505,822 C590,822 660,880 708,944 C650,1010 590,1052 505,1052 C420,1052 350,1010 300,930 Z"/>
    <text class="card-text back-company" x="492" y="850" text-anchor="middle">Grainite Ridge Holdings LLC</text>
  </g>
</svg>
</body>
</html>
```